Kindle Book Cover for Teen Financial Niche

Had a temporary cover done for the book but it needs a lot better cover now it is starting to get some traction.
The current book can be seen here:
https://www.bookvalemart.com/dp/Q7K42LZ9RT
I am wanting something very different if possible. Please search books in the teen financial niche on Bookvale and you will see that a lot of the covers are very similar in style.
I am looking for something different that will stand out in a crowded marketplace.
If you are putting someone on the cover please use a male character rather than a female one.
Thanks
Dale

```html
<!DOCTYPE html>
<html lang="en">
<head>
<meta charset="utf-8">
<title>Everyday Economy for Teen and Young Adults — Book Cover</title>
<link rel="stylesheet" href="https://fonts.googleapis.com/css2?family=Delius&family=Quicksand:wght@500&display=swap">
<style>
  :root {
    --canvas: #ffffff;
    --felt-green: #3fae2a;
    --felt-green-dark: #2f9620;
    --paper: #ffffff;
    --rule: #cacacd;
    --rule-strong: #b9b9bc;
    --ink-blue: #14148c;
    --marker-orange: #f5a21e;
    --marker-orange-dark: #e08b14;
    --pen-red: #d4182a;
    --tape-green: #a9da93;
    --tape-green-dark: #93c97c;
  }
  * { box-sizing: border-box; margin: 0; padding: 0; }
  html, body {
    width: 1200px; height: 1000px; overflow: hidden;
    background: var(--canvas);
  }
  .book-cover {
    position: absolute;
    left: 338px; top: 79px;
    width: 525px; height: 842px;
    overflow: hidden;
    background: radial-gradient(circle at 30% 40%, var(--felt-green) 0%, var(--felt-green-dark) 140%);
  }
  .notebook-page {
    position: absolute;
    left: 22px; top: 15px;
    width: 513px; height: 740px;
    transform: rotate(-4deg);
    transform-origin: 50% 50%;
    background:
      linear-gradient(115deg, rgba(255,255,255,0) 40%, rgba(210,210,214,0.55) 75%, rgba(200,200,204,0.75) 100%),
      repeating-linear-gradient(to bottom, transparent 0 36px, var(--rule) 36px 37px),
      var(--paper);
    background-position: 0 0, 0 22px, 0 0;
    box-shadow: 0 2px 6px rgba(0,0,0,0.25);
  }
  .page-rule-top {
    position: absolute; left: 8px; right: 20px; top: 54px;
    height: 6px;
    border-top: 2px solid var(--rule-strong);
    border-bottom: 2px solid var(--rule-strong);
  }
  .page-rule-bottom {
    position: absolute; left: 46px; right: 0; top: 696px;
    height: 3px; background: var(--rule-strong);
  }
  .title {
    position: absolute; left: 48px; top: 52px;
    font-family: "Delius", cursive;
    color: var(--ink-blue);
    font-size: 104px; line-height: 106px;
    font-weight: 400;
    white-space: nowrap;
  }
  .title span { display: block; }
  .title .line-two { margin-left: 8px; }
  .audience-band {
    position: absolute; left: 28px; top: 292px;
    width: 394px; height: 44px;
    transform: rotate(-2.5deg);
    background: linear-gradient(90deg, var(--marker-orange) 0%, var(--marker-orange) 65%, var(--marker-orange-dark) 100%);
    border-radius: 3px 14px 5px 10px;
  }
  .audience {
    position: absolute; left: 56px; top: 292px;
    transform: rotate(-2.5deg);
    font-family: "Delius", cursive;
    color: var(--ink-blue);
    font-size: 27px; line-height: 40px;
    white-space: nowrap;
  }
  .dollar-artwork {
    position: absolute; left: 24px; top: 362px;
    width: 290px; height: 330px;
    border-radius: 50%;
    background: radial-gradient(circle at 50% 48%, rgba(20,20,140,0.24) 0%, rgba(20,20,140,0.1) 45%, rgba(20,20,140,0) 70%);
  }
  .series {
    position: absolute; left: 250px; top: 352px;
    font-family: "Quicksand", sans-serif;
    font-weight: 500;
    color: var(--ink-blue);
    font-size: 22px; line-height: 28px;
    letter-spacing: 0.5px;
    white-space: nowrap;
  }
  .roadmap {
    position: absolute; left: 294px; top: 396px;
    font-family: "Delius", cursive;
    color: var(--ink-blue);
    font-size: 20px; line-height: 26px;
    white-space: nowrap;
  }
  .topic-list {
    position: absolute; left: 298px; top: 434px;
    list-style: none;
    font-family: "Delius", cursive;
    color: var(--ink-blue);
    font-size: 16.5px;
  }
  .topic-list li {
    height: 37px; line-height: 26px;
    display: flex; align-items: center; gap: 6px;
    white-space: nowrap;
  }
  .topic-list .check-circle {
    width: 9px; height: 9px;
    border: 1.5px solid var(--pen-red);
    border-radius: 50%;
    flex: none;
  }
  .author-label {
    position: absolute; left: 158px; top: 751px;
    width: 325px; height: 63px;
    background: linear-gradient(90deg, var(--tape-green) 0 61px, var(--tape-green-dark) 61px 100%);
    box-shadow: 0 2px 4px rgba(0,0,0,0.2);
    display: flex; align-items: center; justify-content: flex-end;
    padding-right: 30px;
    font-family: "Delius", cursive;
    color: var(--ink-blue);
    font-size: 36px;
    white-space: nowrap;
  }
</style>
</head>
<body>
  <main class="book-cover">
    <section class="notebook-page">
      <div class="page-rule-top"></div>
      <h1 class="title">
        <span class="line-one">Everyday</span>
        <span class="line-two">Economy</span>
      </h1>
      <div class="audience-band"></div>
      <p class="audience">for Teen and Young Adults</p>
      <div class="dollar-artwork" role="img" aria-label="Hand-sketched blue dollar sign with burst lines around it"></div>
      <p class="series">CASH COMPASS</p>
      <p class="roadmap">A roadmap to :</p>
      <ul class="topic-list">
        <li><span class="check-circle"></span>earning power</li>
        <li><span class="check-circle"></span>wise spending</li>
        <li><span class="check-circle"></span>budgeting</li>
        <li><span class="check-circle"></span>saving</li>
        <li><span class="check-circle"></span>investing</li>
      </ul>
      <div class="page-rule-bottom"></div>
    </section>
    <p class="author-label">Liam Carvalho</p>
  </main>
</body>
</html>
```